Broschüre für externen Datenschutzpartner
Herzlichen Dank an KoLuxAr für die ausgezeichneten Arbeiten und das perfekte Ergebnis.
Zielgruppe
Korvento hat sich darauf spezialisiert, insbesondere kleine und mittelständische Unternehmen als externer Datenschutzpartner kontinuierlich zu betreuen und zu beraten. Durch neue Anforderungen – bereits heute durch die DS-GVO und zukünftig durch die EPVO – wird es zunehmend notwendig für Unternehmen, verstärkt externe Beratung mit entsprechendem Know-how in den Bereichen Datenschutz und IT-Sicherheit einzuholen. Denn der Schutz personenbezogener Daten sowie die geforderte Sicherheit haben durch die Gültigkeit der europaweit geltenden DS-GVO massiv an Bedeutung gewonnen. Dieser Trend wird durch die zunehmende Digitalisierung weiter zunehmen. Hier bieten wir ein breites Leistungsspektrum an.
Aufgabenstellung
Eine Broschüre als Vorlage ist beigefügt. (Brisalt-Info-NetzwerkAblauf.pdf) Es sollen ebenso alle relevanten Informationen auf die Seiten verteilt werden, ohne die Seiten zu überladen. Bei den Grafiken würden wir uns ähnliche Bilder (StockPhotos) wünschen. Die vorhandene CI der Korvento (www.korvento.de) soll dabei wieder zu erkennen sein.
Alle weiteren Informationen sind den beigefügten Dokumenten und der Website zu entnehmen. Die Broschüre soll das Präsentation dargestellt werden. zwischen 7-9 Seiten. Inhaltliche Fragen werden jederzeit beantwortet.

```html
<!DOCTYPE html>
<html lang="de">
<head>
<meta charset="utf-8">
<title>Korvento – Broschüre IT-Sicherheit &amp; Datenschutz</title>
<link href="https://fonts.googleapis.com/css2?family=Quicksand:wght@400;500;600;700&display=swap" rel="stylesheet">
<style>
:root{
  --stage:#e9e9e9;
  --green:#3aa84a;
  --green-dark:#2e8f3d;
  --ink:#4a4a4a;
  --ink-soft:#6d6d6d;
  --dark-band:#4d4d4f;
  --paper:#ffffff;
  --paper-grey:#f1f1f1;
  --card:#dcdcdc;
  --card-head:#8a8a8a;
}
*{box-sizing:border-box;margin:0;padding:0}
html,body{width:1200px;height:3648px;overflow:hidden;background:var(--stage);font-family:'Quicksand',sans-serif;color:var(--ink)}
.canvas{position:relative;width:1200px;height:3648px}
.page{position:absolute;background:var(--paper);overflow:hidden}
.abs{position:absolute}
.photo{position:absolute}
.small{font-size:6.6px;line-height:1.45;color:var(--ink-soft)}
.small p{margin-bottom:6px}
.heading{font-weight:500;letter-spacing:.3px;color:var(--ink);text-transform:uppercase}
.heading b{font-weight:700}
.white{color:#fff}
.white .small,.small.white{color:#fff}

/* Cover */
.cover{left:282px;top:77px;width:633px;height:447px;background:linear-gradient(135deg,#f6f6f6,#e4e4e4)}
.cover .brand{left:28px;top:26px;display:flex;align-items:center;gap:8px}
.cover .brand-dot{width:14px;height:14px;border-radius:50%;background:var(--green)}
.cover .brand-name{font-size:46px;font-weight:600;color:var(--ink);letter-spacing:-.5px;line-height:1}
.cover .brand-tag{left:54px;top:82px;font-size:9.5px;font-weight:600;color:var(--ink)}
.cover .title-band{left:0;top:311px;width:300px;height:136px;background:var(--dark-band)}
.cover .title{left:32px;top:342px;font-size:28px;font-weight:500;color:#fff;line-height:1.25}

/* Konzept */
.konzept{left:282px;top:570px;width:633px;height:447px}
.konzept .side{left:0;top:0;width:242px;height:447px;background:var(--green)}
.konzept .side .heading{position:absolute;left:37px;top:66px;font-size:14px;color:#fff}
.konzept .side .rule{position:absolute;left:37px;top:90px;width:150px;height:1px;background:rgba(255,255,255,.7)}
.konzept .side .small{position:absolute;left:37px;top:112px;width:175px}
.konzept .col{top:318px;width:170px}

/* Vorteile */
.vorteile{left:282px;top:1073px;width:633px;height:447px;background:linear-gradient(180deg,#fbfbfb,#efefef);border-top:4px solid var(--green)}
.box{position:absolute;background:#fff;border:1.5px solid #555;border-radius:10px;padding:8px 12px}
.box h4{font-size:9.5px;font-weight:600;text-transform:uppercase;color:var(--ink);border-bottom:1px solid var(--green);padding-bottom:3px;margin-bottom:4px}
.box.center h4{text-align:center}
.box .small{font-size:5.8px}
.box.center .small{text-align:center}
.badge{position:absolute;width:32px;height:32px;border-radius:50%;background:#fff;border:3px solid var(--green)}
.vorteile .core{left:260px;top:180px;width:120px;text-align:center;font-size:15px;font-weight:500;line-height:1.1;color:var(--ink)}

/* Prinzipien */
.prinzip{left:282px;top:1573px;width:633px;height:446px}
.prinzip .title{left:0;top:76px;width:633px;text-align:center;font-size:20px;font-weight:500;color:#fff;letter-spacing:.5px}
.pillar{position:absolute;top:248px;width:180px;text-align:center}
.pillar h3{font-size:16px;font-weight:500;line-height:1.15;text-transform:uppercase;color:var(--ink)}
.pillar h3 b{font-weight:700}
.pillar .small{font-size:9.6px;line-height:1.45;color:var(--ink);margin-top:16px}
.pillar .accent{color:var(--green);font-weight:700}

/* Kultur */
.kultur{left:293px;top:2077px;width:631px;height:445px}
.kultur .side{left:387px;top:0;width:244px;height:445px;background:var(--green)}
.kultur .side .heading{position:absolute;left:38px;top:66px;font-size:14px;color:#fff}
.kultur .side .rule{position:absolute;left:38px;top:90px;width:150px;height:1px;background:rgba(255,255,255,.7)}
.kultur .side .small{position:absolute;left:38px;top:112px;width:170px}

/* Pakete */
.pakete{left:293px;top:2576px;width:638px;height:446px}
.pakete .title{left:0;top:150px;width:638px;text-align:center;font-size:20px;font-weight:500;color:#fff;letter-spacing:.4px}
.card{position:absolute;top:296px;width:121px;height:122px;background:var(--card)}
.card .head{height:20px;background:var(--card-head);color:#fff;font-size:9.5px;font-weight:500;text-align:center;line-height:20px;text-transform:uppercase}
.card.xl .head{background:var(--green)}
.card ul{list-style:none;padding:6px 10px}
.card li{font-size:5.6px;text-align:center;color:var(--ink-soft);text-transform:uppercase;padding:3px 0;border-bottom:1px solid #c6c6c6}
.card li:last-child{border-bottom:0}
.price{position:absolute;top:252px;width:50px;height:48px}
.price span{position:absolute;left:0;top:14px;width:50px;text-align:center;font-size:14px;font-weight:500;color:var(--ink)}

/* Zielgruppe */
.ziel{left:309px;top:3089px;width:628px;height:443px;border-top:8px solid var(--green)}
.ziel .heading{position:absolute;font-size:14px}
.ziel .step{position:absolute;left:26px;display:flex;gap:14px;width:400px}
.ziel .num{flex:none;width:22px;height:22px;border:1.5px solid var(--green);border-radius:50%;font-size:11px;text-align:center;line-height:19px;color:var(--ink);background:#fff}
.ziel .step .small{font-size:7px;padding-top:2px}
.ziel .band{left:0;top:234px;width:628px;height:209px;background:var(--green)}
.ziel .cta-tag{left:448px;top:26px;background:var(--card-head);color:#fff;font-size:6.5px;padding:2px 4px;text-transform:uppercase}
.ziel .cta{left:462px;top:38px;background:var(--dark-band);color:#fff;font-size:12px;padding:4px 8px;display:flex;align-items:center;gap:6px}
</style>
</head>
<body>
<div class="canvas">

  <!-- Cover -->
  <section class="page cover">
    <div class="abs brand"><span class="brand-dot"></span><span class="brand-name">Korvento</span></div>
    <div class="abs brand-tag">Professioneller Datenschutz für Unternehmen</div>
    <div class="abs title-band"></div>
    <svg class="abs" style="left:250px;top:0" width="383" height="447" viewBox="0 0 383 447">
      <defs>
        <linearGradient id="knightCover" x1="0" y1="0" x2="1" y2="1">
          <stop offset="0" stop-color="#c9ccd0"/><stop offset=".55" stop-color="#6e7378"/><stop offset="1" stop-color="#3e4246"/>
        </linearGradient>
      </defs>
      <path d="M70 150 Q150 120 240 70 L383 10 L383 447 L200 447 Q90 380 70 250 Z" fill="var(--green)"/>
      <path role="img" aria-label="Foto: Ritter in Rüstung mit grünem Schild" d="M92 165 Q165 138 245 92 L383 34 L383 447 L212 447 Q108 380 92 252 Z" fill="url(#knightCover)"/>
    </svg>
    <div class="abs title">IT-SICHERHEIT &amp;<br>DATENSCHUTZ</div>
  </section>

  <!-- Konzept / Aufgaben -->
  <section class="page konzept">
    <div class="abs side">
      <div class="heading">Unser <b>Konzept</b></div>
      <div class="rule"></div>
      <div class="small white">
        <p>Die Korvento GmbH &amp; Co. KG ist ein junges, dynamisches Beratungsunternehmen mit Sitz im Herzen von Elbhausen. Korvento hat sich darauf spezialisiert, insbesondere kleine und mittelständische Unternehmen als externer Datenschutzpartner kontinuierlich zu betreuen und zu beraten.</p>
        <p>Durch neue Anforderungen – bereits heute durch die DS-GVO und zukünftig durch die EPVO – wird es zunehmend notwendig für Unternehmen, verstärkt externe Beratung mit entsprechendem Know-how in den Bereichen Datenschutz und IT-Sicherheit einzuholen.</p>
        <p>Denn der Schutz personenbezogener Daten sowie die geforderte Sicherheit haben durch die Gültigkeit der europaweit geltenden DS-GVO massiv an Bedeutung gewonnen. Dieser Trend wird durch die zunehmende Digitalisierung weiter zunehmen.</p>
        <p><b>HIER BIETEN WIR EIN BREITES LEISTUNGSSPEKTRUM AN.</b></p>
      </div>
    </div>
    <div class="photo" role="img" aria-label="Foto: Ritter mit Schwert und grünem Schild" style="left:242px;top:23px;width:391px;height:222px;background:linear-gradient(120deg,#dfe3ea,#aab1bb 55%,#5d636a)"></div>
    <div class="abs heading" style="left:280px;top:272px;font-size:14px">Unsere <b>Aufgaben</b></div>
    <div class="abs small col" style="left:280px">Als Anbieter für externen Datenschutz und IT-Sicherheit verfügt Korvento über eine hochwertige inhaltliche sowie technische Expertise und bildet damit das Fundament für die Einhaltung der DS-GVO und der zukünftigen EPVO in Unternehmen bis zu einer mittelständischen Größe. Wir helfen Ihnen dabei, die neue DS-GVO und die EPVO problemlos in Ihrem Unternehmen zu integrieren.</div>
    <div class="abs small col" style="left:458px">Zudem beraten wir Sie fortlaufend, um eine pragmatische Umsetzung der Anforderungen im Bereich Datenschutz zu gewährleisten.<br><br>Dazu zählen auch <b>notwendige technische und organisatorische Maßnahmen.</b> Als externe Datenschutzbeauftragte bringen wir die nötige Expertise mit, um Ihr Unternehmen zu beraten.</div>
  </section>

  <!-- Vorteile -->
  <section class="page vorteile">
    <svg class="abs" style="left:0;top:0" width="633" height="443" viewBox="0 0 633 443" fill="none" stroke="#555" stroke-width="1.5">
      <line x1="316" y1="108" x2="316" y2="175"/>
      <line x1="316" y1="245" x2="316" y2="324"/>
      <path d="M228 170 H288 V195"/><path d="M401 170 H345 V195"/>
      <path d="M228 275 H288 V245"/><path d="M401 275 H345 V245"/>
    </svg>
    <div class="box center" style="left:221px;top:24px;width:191px;height:86px">
      <h4>Kompetenz</h4>
      <div class="small">Datenschutz ist ein sehr umfassendes Thema und bereitet noch vielen Unternehmen Schwierigkeiten. Wir gehen das Thema strukturiert und mit genügend Fachexpertise für Sie an.</div>
    </div>
    <div class="box" style="left:37px;top:118px;width:191px;height:102px">
      <h4>Betreuung</h4>
      <div class="small">Unsere Handlungsempfehlungen und alle zukünftigen Maßnahmen werden von uns erfolgreich umgesetzt. Eine kontinuierliche Betreuung sehen wir als selbstverständlich an – nur so sind Unternehmen auch langfristig erfolgreich geschützt.</div>
    </div>
    <div class="box" style="left:401px;top:118px;width:196px;height:94px">
      <h4>Fokus</h4>
      <div class="small">Fokus DSGVO und e-Privacy: Gemeinsam übernehmen wir die Hürden der neuen Datenschutzgesetze und konzentrieren uns zielgerichtet auf Ihr Unternehmen.</div>
    </div>
    <div class="box" style="left:37px;top:228px;width:191px;height:91px">
      <h4>Technologie</h4>
      <div class="small">Dank unserer Webplattform werden Ihnen zeit- &amp; materialsparende Prozesse geboten. Durch unsere KOrvento[S]chutz[P]rotect[A]pplication (KOSPA) erkennen wir schnell das Problem und handeln ohne Umwege.</div>
    </div>
    <div class="box" style="left:401px;top:225px;width:196px;height:89px">
      <h4>Partnerschaft</h4>
      <div class="small">Die Formel für eine optimale Kundenbeziehung ist der Erfolg, der sich aus Vertrauen und Problemverständnis zusammensetzt. Durch unsere Betreuung stehen Ihnen unsere volle Kompetenz und unser Expertenwissen zur Verfügung.</div>
    </div>
    <div class="box center" style="left:221px;top:324px;width:191px;height:93px">
      <h4 style="margin-top:14px">Transparenz</h4>
      <div class="small">Durch unsere individuellen Leistungspakete bekommen Sie den passenden Schutz ohne versteckte Extrakosten. Ein transparentes und faires Angebot sehen wir als einen essenziellen Bestandteil für einen externen Datenschutzbeauftragten.</div>
    </div>
    <div class="abs core">IHRE<br>VORTEILE</div>
    <div class="badge" style="left:300px;top:92px"></div>
    <div class="badge" style="left:212px;top:154px"></div>
    <div class="badge" style="left:385px;top:154px"></div>
    <div class="badge" style="left:212px;top:259px"></div>
    <div class="badge" style="left:385px;top:255px"></div>
    <div class="badge" style="left:300px;top:310px"></div>
  </section>

  <!-- Prinzipien -->
  <section class="page prinzip">
    <div class="photo" role="img" aria-label="Foto: Ritter in Rüstung, dunkel getönt" style="left:0;top:0;width:633px;height:196px;background:linear-gradient(90deg,#4a4b4d,#5b5d60 55%,#3f4042)"></div>
    <div class="abs title">PRAGMATISCH. SICHER. KOMPETENT!</div>
    <svg class="abs" style="left:72px;top:150px" width="490" height="90" viewBox="0 0 490 90">
      <g fill="#fff" stroke="var(--green)" stroke-width="5">
        <path d="M43 4 L80 18 Q80 65 43 84 Q6 65 6 18 Z"/>
        <path d="M240 4 L277 18 Q277 65 240 84 Q203 65 203 18 Z"/>
        <path d="M438 4 L475 18 Q475 65 438 84 Q401 65 401 18 Z"/>
      </g>
      <g fill="var(--green)">
        <circle cx="43" cy="38" r="11"/><rect x="37" y="50" width="12" height="8" rx="2"/>
        <circle cx="235" cy="38" r="10"/><circle cx="250" cy="52" r="7"/>
      </g>
      <g fill="none" stroke="var(--green)" stroke-width="4">
        <circle cx="434" cy="40" r="12"/><line x1="443" y1="49" x2="454" y2="60"/>
        <path d="M428 40 l5 5 l8 -9" stroke-width="3"/>
      </g>
    </svg>
    <div class="pillar" style="left:25px"><h3>Warum<br><b>Korvento?</b></h3>
      <div class="small">Wir rüsten Sie gegen Bedrohungen durch IT und Cyber Kriminalität sowie Datenklau und bieten die perfekte Betreuung, ganz gleich ob DS-GVO oder EPVO! Durch PRÜFSIEGEL-geprüfte und zertifizierte Mitarbeiter.</div></div>
    <div class="pillar" style="left:222px"><h3>Unsere<br><b>Maßnahmen</b></h3>
      <div class="small">Passende Leistungspakete für jedes Unternehmen. Wir helfen Ihnen die neue DSGVO in Ihrem Unternehmen problemlos zu integrieren. Wir beraten sowohl kleine als auch mittelständische Unternehmen für eine optimale Umsetzung.</div></div>
    <div class="pillar" style="left:420px"><h3>Unsere<br><b>Kontrolle</b></h3>
      <div class="small"><span class="accent">VERTRAUEN IST GUT –<br>KONTROLLE IST BESSER!</span><br>Durch externe Datenschutzbeauftragte gewinnen Sie das Vertrauen Ihrer Kunden und vermeiden unnötige Abmahnungen durch unseren Schild-Check (KOSPA).</div></div>
  </section>

  <!-- Arbeiten / Kultur -->
  <section class="page kultur">
    <div class="photo" role="img" aria-label="Foto: Hände an einem Laptop im Büro" style="left:0;top:22px;width:387px;height:194px;background:linear-gradient(110deg,#b9c6d3,#e6ecf1 45%,#8e9aa6)"></div>
    <div class="abs heading" style="left:26px;top:250px;font-size:14px">Unsere <b>Arbeiten</b></div>
    <div class="abs" style="left:26px;top:274px;width:150px;height:1px;background:var(--green)"></div>
    <div class="abs small" style="left:26px;top:300px;width:170px">Unsere Datenschutzexperten vereinbaren zunächst einen Termin mit Ihnen und kommen persönlich in Ihr Unternehmen. Bei diesem detaillierten Datenschutz-Audit stellen wir den notwendigen Handlungsbedarf fest und begleiten Sie kompetent und pragmatisch bei den erforderlichen Maßnahmen. Wir sind sowohl intern als auch extern der erste Ansprechpartner, wenn es um Datenschutz und IT-Sicherheit geht.</div>
    <div class="abs small" style="left:204px;top:300px;width:165px">Durch unsere Kundenplattform bieten wir Ihnen darüber hinaus zeit- und materialsparende Prozesse an. Einen ersten Check Ihrer Website werden wir zukünftig durch den Einsatz unserer geplanten <span style="color:var(--green)">KOrvento[S]chutz[P]rotect[A]pplication</span> vornehmen können. Somit kommt es nicht zu unnötigen Abmahnungen.</div>
    <div class="abs side">
      <div class="heading">Unsere <b>Kultur</b></div>
      <div class="rule"></div>
      <div class="small white">
        <p>Wir sind stets positiv eingestellt, gehen respektvoll miteinander um und arbeiten pragmatisch und hoch professionell.</p>
        <p>Teamarbeit und persönliche Wertschätzung stehen bei uns an erster Stelle.</p>
        <p>Dazu zählt persönliche Leistung genauso wie Eigenständigkeit.</p>
        <p>Die Formel für eine <b>optimale Kundenbeziehung</b> ist der Erfolg, der sich aus Vertrauen und Problemverständnis zusammensetzt – durch unsere Betreuung stehen Ihnen unsere gesamte Kompetenz und unser Expertenwissen für maximalen Erfolg zur Verfügung.</p>
      </div>
    </div>
  </section>

  <!-- Leistungspakete -->
  <section class="page pakete">
    <div class="photo" role="img" aria-label="Foto: Ritter mit Schwert und Schild, grün getönt" style="left:0;top:0;width:638px;height:262px;background:linear-gradient(90deg,#3aa84a,#2f8d3d 50%,#3aa84a)"></div>
    <div class="abs title">DAS FÜR SIE PASSENDE LEISTUNGSPAKET</div>
    <div class="card" style="left:34px"><div class="head">Leistung S</div><ul><li>Einzelhandel</li><li>Gastronomie</li><li>KFZ Betriebe</li><li>Handwerksbetriebe</li><li>Baugewerbe</li></ul></div>
    <div class="card" style="left:184px"><div class="head" style="background:#6a6a6a">Leistung M</div><ul><li>Agenturen &amp; Makler</li><li>Werbebranche</li><li>Ärzte und Apotheker</li><li>Online Shops/E-Commerce</li><li>Transport &amp; Logistik</li></ul></div>
    <div class="card" style="left:336px"><div class="head">Leistung L</div><ul><li>Medizin und</li><li>Gesundheitswesen</li><li>Steuerberater</li><li>Medienunternehmen</li><li>Marketing</li></ul></div>
    <div class="card xl" style="left:487px"><div class="head">Leistung XL</div><ul><li>KMU's mit über 100 MA</li><li>Personal-Service</li><li>Finanzdienstleister</li><li>Produzierendes Gewerbe</li><li>Industrie</li></ul></div>
    <svg width="0" height="0" style="position:absolute"><defs><path id="priceShield" d="M25 2 L48 11 Q48 38 25 47 Q2 38 2 11 Z"/></defs></svg>
    <div class="price" style="left:69px"><svg width="50" height="48"><use href="#priceShield" fill="#fff" stroke="var(--green)" stroke-width="3"/></svg><span>150€</span></div>
    <div class="price" style="left:219px"><svg width="50" height="48"><use href="#priceShield" fill="#fff" stroke="var(--green)" stroke-width="3"/></svg><span>250€</span></div>
    <div class="price" style="left:371px"><svg width="50" height="48"><use href="#priceShield" fill="#fff" stroke="var(--green)" stroke-width="3"/></svg><span>350€</span></div>
    <div class="price" style="left:522px"><svg width="50" height="48"><use href="#priceShield" fill="#fff" stroke="var(--green)" stroke-width="3"/></svg><span>500€</span></div>
  </section>

  <!-- Zielgruppe -->
  <section class="page ziel">
    <div class="heading" style="left:26px;top:34px">Wer braucht Datenschutz?</div>
    <div class="abs" style="left:26px;top:56px;width:380px;height:1px;background:#ccc"></div>
    <div class="abs cta-tag">Worauf warten Sie?</div>
    <div class="abs cta">
      <svg width="12" height="12" viewBox="0 0 24 24"><path fill="#fff" d="M6.6 10.8a15 15 0 0 0 6.6 6.6l2.2-2.2c.3-.3.7-.4 1-.2 1.1.4 2.3.6 3.6.6.6 0 1 .4 1 1V20c0 .6-.4 1-1 1A17 17 0 0 1 3 4c0-.6.4-1 1-1h3.5c.6 0 1 .4 1 1 0 1.3.2 2.5.6 3.6.1.3 0 .7-.2 1z"/></svg>
      0340 7700 18 27 0
    </div>
    <div class="step" style="top:74px"><span class="num">1</span><div class="small">Privatrechtliche Organisationen und Firmen, aber auch Personen, die personenbezogene Daten verarbeiten (z.B.: Selbstständige, Produktions-, Handels- und Dienstleistungsunternehmen)</div></div>
    <div class="step" style="top:128px"><span class="num">2</span><div class="small">Sonstige Privatrechtliche Organisationen, deren Geschäftszweck die Verarbeitung personenbezogener Daten für Fremde ist (z.B.: Service-Rechenzentren oder Forschungseinrichtungen)</div></div>
    <div class="step" style="top:180px"><span class="num">3</span><div class="small">Öffentliche Stellen des Bundes und der Länder (z.B.: Bundesbehörden oder Kommunalverwaltungen)</div></div>
    <div class="abs band"></div>
    <div class="heading white" style="left:26px;top:262px;color:#fff">Warum Korvento?</div>
    <div class="abs" style="left:26px;top:284px;width:380px;height:1px;background:rgba(255,255,255,.7)"></div>
    <div class="abs small white" style="left:26px;top:298px;width:400px">
      <p>Wir gewährleisten eine fehlerfreie Implementierung und Einhaltung eines ausreichenden Datenschutzes einschließlich der notwendigen technischen Voraussetzung.</p>
      <p>Zudem betreuen wir Sie kontinuierlich dahingehend, dass alle Abläufe den gesetzlichen Anforderungen gerecht werden und beugen somit aktiv Datenschutzverstößen vor.</p>
      <p>Unsere individualisierten Leistungspakete, die für jede Unternehmensgröße die optimale Betreuung bieten, sind auf Ihre speziellen Anforderungen abgestimmt.</p>
      <p>Sämtliche Leistungen sind auch individuell buchbar. Ein transparentes und faires Angebot ist für uns essenzieller Bestandteil einer kompetenten Beratung im Bereich Datenschutz und IT-Sicherheit.</p>
    </div>
    <div class="photo" role="img" aria-label="Foto: Ritter in Rüstung mit grünem Schild" style="left:440px;top:80px;width:188px;height:355px;background:linear-gradient(160deg,#d5d8dc,#7b8086 50%,#3b3f43);clip-path:polygon(35% 0,75% 0,100% 20%,100% 100%,0 100%,8% 40%)"></div>
  </section>

</div>
</body>
</html>
```